Business Card Design Project

Refresh of logo attached. Require text underneath to be more ledgible, crisper & cleaner.

Overall, staying with same colour scheme need a brighter, crisper, easily readible business card style.

Industry/Entity Type

Business

```html
<!DOCTYPE html>
<html lang="en">
<head>
<meta charset="utf-8">
<title>Halden Business Card</title>
<link rel="stylesheet" href="https://fonts.googleapis.com/css2?family=Lato:wght@300;400;700&family=Montserrat:wght@700&display=swap">
<style>
  :root {
    --page: #e9ebec;
    --card-light: #fbfbfb;
    --card-shade: #e6e8e9;
    --teal: #4a8ea4;
    --teal-deep: #2f6a80;
    --navy-band: #1f4c5f;
    --ink: #2b3a44;
    --ink-soft: #3f4c55;
    --accent: #4a93b3;
    --band-text: #e3eef2;
  }
  * { box-sizing: border-box; margin: 0; padding: 0; }
  html, body {
    width: 1200px; height: 900px; overflow: hidden;
    background: var(--page);
    font-family: "Lato", Arial, sans-serif;
  }
  .canvas { position: relative; width: 1200px; height: 900px; }

  .card {
    position: absolute;
    width: 640px; height: 366px;
    background: linear-gradient(150deg, var(--card-light) 0%, #f1f2f3 55%, var(--card-shade) 100%);
    box-shadow: 0 10px 30px rgba(30, 40, 50, 0.18);
    overflow: hidden;
  }

  /* Contact side */
  .card--contact { left: 110px; top: 56px; }
  .identity {
    position: absolute; right: 58px; top: 46px;
    display: flex; align-items: center; gap: 18px;
  }
  .identity__square { width: 34px; height: 34px; background: var(--teal); }
  .identity__name {
    font-family: "Montserrat", Arial, sans-serif;
    font-weight: 700; font-size: 21px; letter-spacing: 0.5px;
    color: var(--teal-deep);
  }
  .identity__role {
    font-size: 14px; font-weight: 400; letter-spacing: 0.4px;
    color: var(--accent); margin-top: 4px;
  }
  .contact-band {
    position: absolute; left: 0; right: 0; bottom: 38px; height: 72px;
    background: linear-gradient(90deg, var(--teal) 0%, #3f7f95 60%, var(--teal-deep) 100%);
    display: flex; align-items: center; justify-content: flex-end;
    gap: 46px; padding-right: 44px;
  }
  .contact-item {
    display: flex; align-items: center; gap: 12px;
    color: var(--band-text); font-size: 14px; letter-spacing: 0.6px;
  }
  .contact-item svg { width: 14px; height: 14px; fill: var(--band-text); }

  /* Brand side */
  .card--brand { left: 450px; top: 478px; }
  .lockup {
    position: absolute; left: 0; right: 0; top: 86px;
    display: flex; flex-direction: column; align-items: center;
  }
  .lockup__mark { display: flex; align-items: center; gap: 18px; }
  .lockup__square { width: 48px; height: 48px; background: var(--teal); }
  .lockup__name {
    font-weight: 400; font-size: 66px; letter-spacing: 1px; line-height: 1;
    color: var(--ink);
  }
  .lockup__rule {
    width: 330px; height: 1px; background: var(--ink-soft); margin-top: 16px;
  }
  .lockup__tagline {
    margin-top: 10px; font-size: 14px; font-weight: 400; letter-spacing: 0.6px;
    color: var(--ink-soft);
  }
  .lockup__tagline-accent { color: var(--accent); }
  .web-band {
    position: absolute; left: 0; right: 0; bottom: 0; height: 62px;
    background: linear-gradient(90deg, var(--teal-deep) 0%, var(--navy-band) 100%);
    display: flex; align-items: center; justify-content: flex-end;
    padding-right: 40px;
    color: var(--band-text); font-size: 14px; letter-spacing: 5px;
  }
</style>
</head>
<body>
<main class="canvas">

  <section class="card card--contact" aria-label="Card back with contact details">
    <div class="identity">
      <span class="identity__square" aria-hidden="true"></span>
      <div>
        <div class="identity__name">EVAN R. TALBOT</div>
        <div class="identity__role">Certified Executive Advisor</div>
      </div>
    </div>
    <div class="contact-band">
      <span class="contact-item">
        <svg viewBox="0 0 24 24" aria-hidden="true"><path d="M6.6 10.8a15.1 15.1 0 0 0 6.6 6.6l2.2-2.2c.3-.3.7-.4 1-.2 1.1.4 2.3.6 3.6.6.6 0 1 .4 1 1V20c0 .6-.4 1-1 1C10.6 21 3 13.4 3 4c0-.6.4-1 1-1h3.5c.6 0 1 .4 1 1 0 1.3.2 2.5.6 3.6.1.3 0 .7-.2 1z"/></svg>
        (555) 014 2387
      </span>
      <span class="contact-item">
        <svg viewBox="0 0 24 24" aria-hidden="true"><path d="M7 1h10a2 2 0 0 1 2 2v18a2 2 0 0 1-2 2H7a2 2 0 0 1-2-2V3a2 2 0 0 1 2-2zm0 3v14h10V4zm5 15.2a1.2 1.2 0 1 0 0 2.4 1.2 1.2 0 0 0 0-2.4z"/></svg>
        (555) 017 4410
      </span>
      <span class="contact-item">
        <svg viewBox="0 0 24 24" aria-hidden="true"><path d="M2 5h20v14H2zm2 2v.4l8 5.2 8-5.2V7zm0 2.8V17h16V9.8l-8 5.2z"/></svg>
        evan@halden.ca
      </span>
    </div>
  </section>

  <section class="card card--brand" aria-label="Card front with organisation name">
    <div class="lockup">
      <div class="lockup__mark">
        <span class="lockup__square" aria-hidden="true"></span>
        <span class="lockup__name">Halden</span>
      </div>
      <span class="lockup__rule" aria-hidden="true"></span>
      <p class="lockup__tagline">Estate Planning &amp; <span class="lockup__tagline-accent">Executor Support</span></p>
    </div>
    <div class="web-band">www.halden.ca</div>
  </section>

</main>
</body>
</html>
```